Software Product Flyer Design

A established czech software company needs a marketing flyer to promote their software product and its modules.
The overall feel of the flyer must to be serious, but also eye-catching, enticing, clever and bold to attract customers.
Unifying graphic element is the new product logo.
The flyer would be A4, colour both sides and folded once (to give 4 pages of A5).
Title page - product logo with module name and module icon, short presentation of the product and list of its key features.
Inside pages - detailed informations with screenshots or graphical schemas.
Back side - informations about technical requirements and user support, contacts (address, phone, fax, e-mail, web pages - no social networks).
Product logo, module icon and some images attached.
Updates
Hello,
Reason: For organizational reasons we extending the deadline by 10 days.
FYI: We have uploaded the new ZIP file with previous version of our flyer.
Attached PDF file with text for inner pages.
Target Market(s)
Existing or new customers like municipalities, public authorities and nonprofit organizations.
Industry/Entity Type
Marketing
Requirements
Must have
- Winning designer must provide a template for Adobe InDesign based on his graphic design.
Avoid to using exotic fonts - in Czech we use Latin Extended characters (like áéěíýůčřžšťďň).
Nice to have
- Using graphic motif from product logo like as attached splash screen.

```html
<!DOCTYPE html>
<html lang="en">
<head>
<meta charset="utf-8">
<title>Veltro – Software Product Flyer</title>
<link rel="stylesheet" href="https://fonts.googleapis.com/css2?family=Didact+Gothic&family=Source+Sans+3:ital,wght@0,400;0,600;0,700;1,700&family=Tinos&display=swap">
<style>
  :root {
    --page-bg: #d9d4cf;
    --orange: #f05a22;
    --orange-muted: #e3662f;
    --orange-deep: #c4461a;
    --slate: #474d55;
    --slate-light: #545a62;
    --slate-dark: #33373d;
    --ink: #1d1d1d;
    --white: #ffffff;
    --paper: #eef0ee;
    --silver-hi: #f4f4f4;
    --silver-lo: #a9acb0;
    --photo-a: #b9c0c8;
    --photo-b: #6b737c;
  }
  * { box-sizing: border-box; margin: 0; padding: 0; }
  html, body { width: 1200px; height: 896px; overflow: hidden; }
  body { background: var(--page-bg); position: relative; font-family: "Didact Gothic", sans-serif; }

  .flyer {
    position: absolute; left: 65px; top: 70px; width: 1070px; height: 756px;
    box-shadow: 0 4px 14px rgba(0,0,0,.35);
  }
  .panel { position: absolute; top: 0; height: 756px; width: 535px; overflow: hidden; }

  /* ---------- Back panel ---------- */
  .panel--back { left: 0; background: var(--orange); }
  .back-upper { position: absolute; left: 0; top: 0; width: 535px; height: 425px; background: var(--orange-muted); }

  .sidebar { position: absolute; left: 38px; top: 0; width: 192px; height: 425px; background: var(--slate); box-shadow: 2px 3px 6px rgba(0,0,0,.35); }
  .sidebar__card { position: absolute; left: 10px; top: 0; width: 172px; height: 416px; background: var(--paper); }
  .sidebar__photo { width: 172px; height: 226px; background: linear-gradient(160deg, #f2f4f6 0%, var(--photo-a) 55%, var(--photo-b) 100%); }
  .feature-list { list-style: none; padding: 14px 8px 0 10px; }
  .feature-list li { position: relative; padding-left: 16px; font-size: 10px; line-height: 11px; color: var(--ink); margin-bottom: 9px; }
  .feature-list li::before { content: ""; position: absolute; left: 0; top: 2px; width: 8px; height: 8px; border-radius: 2px; background: var(--orange); }

  .back-url { position: absolute; left: 57px; top: 438px; font-size: 12px; letter-spacing: 2.2px; color: var(--white); }

  .section { position: absolute; left: 228px; width: 282px; }
  .section__title {
    height: 19px; border-radius: 0 10px 10px 0; padding-left: 37px;
    background: linear-gradient(90deg, rgba(150,50,15,.85) 0%, var(--orange-deep) 35%, var(--orange) 100%);
    font-size: 14px; line-height: 19px; color: var(--ink);
  }
  .section__body { margin: 8px 0 0 37px; width: 225px; font-size: 10.3px; line-height: 12.8px; color: var(--white); text-align: justify; }

  .back-headline { position: absolute; left: 37px; top: 503px; font-family: "Source Sans 3", sans-serif; font-weight: 700; font-style: italic; font-size: 24px; line-height: 34px; color: var(--ink); }

  .promo-photo { position: absolute; left: 272px; top: 470px; width: 194px; height: 131px; border: 3px solid #8a8d91; background: linear-gradient(180deg, #d7d9dc 0%, #8d9399 60%, #2c2f33 100%); box-shadow: 3px 4px 6px rgba(0,0,0,.35); }

  .brand { position: absolute; display: flex; align-items: center; gap: 10px; font-family: "Source Sans 3", sans-serif; font-weight: 700; color: var(--white); }
  .brand__mark { width: 30px; height: 30px; background: var(--white); border-radius: 6px; }
  .brand--back { left: 32px; top: 668px; font-size: 52px; }

  .contact { position: absolute; left: 265px; top: 658px; font-family: "Source Sans 3", sans-serif; font-style: italic; font-size: 12.5px; line-height: 17px; color: var(--white); }
  .contact p:last-child { margin-top: 4px; }

  /* ---------- Front panel ---------- */
  .panel--front { left: 535px; background: var(--slate); }
  .module-icon { position: absolute; left: 145px; top: 35px; width: 235px; height: 200px; border-radius: 6px; background: linear-gradient(180deg, #f7f9fb 0%, #c9d7e6 100%); }
  .module-name { position: absolute; left: 0; width: 535px; top: 265px; text-align: center; font-family: "Tinos", serif; font-size: 14px; letter-spacing: 3.5px; color: var(--white); }
  .front-headline { position: absolute; left: 0; width: 535px; top: 320px; text-align: center; font-family: "Source Sans 3", sans-serif; font-weight: 700; font-style: italic; font-size: 25px; color: var(--white); }

  .intro-band { position: absolute; left: 0; top: 360px; width: 535px; height: 198px; background: var(--slate-light); box-shadow: 0 3px 5px rgba(0,0,0,.3); }
  .intro-text { position: absolute; left: 32px; top: 10px; width: 240px; font-size: 10.2px; line-height: 12.8px; color: var(--white); text-align: justify; }
  .intro-text p + p { margin-top: 9px; }
  .intro-rule { position: absolute; left: 293px; top: 12px; width: 2px; height: 168px; background: var(--orange); }

  .module-tabs { position: absolute; left: 313px; top: 30px; list-style: none; }
  .module-tabs li {
    width: 222px; height: 21px; margin-bottom: 3px; padding-left: 12px;
    border-radius: 8px 0 0 8px;
    background: linear-gradient(180deg, var(--silver-hi) 0%, #d6d8da 50%, var(--silver-lo) 100%);
    font-family: "Source Sans 3", sans-serif; font-weight: 600; font-size: 12.5px; line-height: 21px; color: var(--ink);
  }

  .brand--front { left: 0; width: 535px; justify-content: center; top: 605px; font-size: 60px; }
  .tagline { position: absolute; left: 0; width: 535px; top: 694px; text-align: center; font-size: 14px; letter-spacing: 3.2px; color: var(--white); }
  .front-url { position: absolute; left: 0; width: 535px; top: 716px; text-align: center; font-family: "Source Sans 3", sans-serif; font-style: italic; font-size: 14px; letter-spacing: 4px; color: var(--orange); }
</style>
</head>
<body>
<main class="flyer">

  <section class="panel panel--back">
    <div class="back-upper"></div>

    <aside class="sidebar">
      <div class="sidebar__card">
        <div class="sidebar__photo" role="img" aria-label="Photograph of a smiling business team in suits"></div>
        <ul class="feature-list">
          <li>Lorem ipsum dolor sit amet, consectetur adipisicing elit</li>
          <li>seddo eiusmod tempor incididunt ut labore et</li>
          <li>dolore magna aliqua. Ut enim ad minim veniamquis</li>
          <li>ostrud exercitation ullamco laboris nisi ut aliquip ex ea commodo consequat.</li>
          <li>Duis aute irure dolor in reprehenderit in voluptate velit esse cillum dolore</li>
        </ul>
      </div>
    </aside>

    <div class="section" style="top:30px">
      <h3 class="section__title">Lorem ipsum dolor sit amet</h3>
      <p class="section__body">Lorem ipsum dolor sit amet, consectetur adipisicing elit, seddo eiusmod tempor incididunt ut labore et dolore magna aliqua. Ut enim ad minim veniam, quis nostrud exercitation ullamco laboris nisi ut aliquip ex ea commodo consequat. Duis aute irure dolor</p>
    </div>
    <div class="section" style="top:150px">
      <h3 class="section__title">Lorem ipsum irure</h3>
      <p class="section__body">Duis aute irure dolor in reprehenderit in voluptate velit esse cillum dolore eu fugiat nulla pariatur.</p>
    </div>
    <div class="section" style="top:231px">
      <h3 class="section__title">Lorem ipsum cupidatat</h3>
      <p class="section__body">Excepteur sint occaecat cupidatat non proident, sunt in culpa qui officia deserunt mollit anim id est laborum.</p>
    </div>
    <div class="section" style="top:312px">
      <h3 class="section__title">Lorem ipsum proident</h3>
      <p class="section__body">Excepteur sint occaecat cupidatat non proident, sunt in culpa qui officia deserunt mollit anim id est laborum. Duis aute irure dolor in reprehenderit in voluptate velit esse cillum dolore eu fugiat nulla pariatur.</p>
    </div>

    <p class="back-url">WWW.VELTRO-SOFT.COM</p>

    <h2 class="back-headline">Lorem ipsum dolor<br>sit amet, consect</h2>

    <div class="promo-photo" role="img" aria-label="Photograph of a businesswoman giving two thumbs up"></div>

    <div class="brand brand--back"><span class="brand__mark"></span>Veltro</div>

    <address class="contact">
      <p>P : 0123.456.789</p>
      <p>F : 0123.456.789</p>
      <p>E : info@veltro-soft.com</p>
      <p>Suite300, Cityname, Countryname 0000.</p>
    </address>
  </section>

  <section class="panel panel--front">
    <div class="module-icon" role="img" aria-label="Module icon: a spiral-bound address book with coloured index tabs and a large letter on its cover"></div>
    <p class="module-name">00000 SOFTWARE</p>

    <h1 class="front-headline">Lorem ipsum dolor sit amet, consect</h1>

    <div class="intro-band">
      <div class="intro-text">
        <p>Lorem ipsum dolor sit amet, consectetur adipisicing elit, seddo eiusmod tempor incididunt ut labore et dolore magna aliqua. Ut enim ad minim veniam, quis nostrud exercitation ullamco laboris nisi ut aliquip ex ea commodo consequat. Duis aute irure dolor in reprehenderit in voluptate velit esse cillum dolore eu fugiat nulla pariatur.</p>
        <p>Duis aute irure dolor in reprehenderit in voluptate velit esse cillum dolore eu fugiat nulla pariatur. Excepteur sint occaecat cupidatat non proident, sunt in culpa qui officia deserunt mollit anim id est laborum.</p>
      </div>
      <div class="intro-rule"></div>
      <ul class="module-tabs">
        <li>Lorem ipsum dolor sit amet</li>
        <li>Lorem ipsum dolor sit amet</li>
        <li>Lorem ipsum dolor sit amet</li>
        <li>Lorem ipsum dolor sit amet</li>
        <li>Lorem ipsum dolor sit amet</li>
        <li>Lorem ipsum dolor sit amet</li>
      </ul>
    </div>

    <div class="brand brand--front"><span class="brand__mark"></span>Veltro</div>
    <p class="tagline">CZECH SOFTWARE COMPANY</p>
    <p class="front-url">www.veltro-soft.com</p>
  </section>

</main>
</body>
</html>
```